The ONLY 100% Free Security System

We are a national home/auto insurance agency that will be offering home security systems. Our "pitch" is that we will show people (before signing any agreements) how much they can save on their home/auto insurance based on having a security system installed. This is often enough to completely offset the cost of the monthly monitoring fee. One side of the flyer will highlight "The ONLY 100% truly free security system". The other side will list the following bullet points: 1. $100's in FREE Premium Security Equipment 2. FREE Professional Installation 3. "and what no other company offers..." ZERO Cost Monitoring (up to a $74.95 per month value) How? Call our 24-hour message line for a 2-minute overview: (phone # needs to be editable)

The last bullet point (what no other company offers... ZERO cost monitoring) needs to stand out.

Target Market(s)

Homeowners and businesses

Industry/Entity Type

Insurance

Font styles to use
Serif
Sans Serif

Colors

Designer to choose colors to be used in the design.

Requirements
Must have
• Editable phone # - this is also a 5.5"(width) X 8.5" (length) flyer

```html
<!DOCTYPE html>
<html lang="en">
<head>
<meta charset="utf-8">
<title>Shieldwell – 100% Free Security System Flyer</title>
<link href="https://fonts.googleapis.com/css2?family=Montserrat:wght@400;600;700;800;900&family=Roboto:wght@400;500;700;900&display=swap" rel="stylesheet">
<style>
  :root{
    --bg:#5a5a5a;
    --blue:#1d4fa3;
    --blue-dark:#143c86;
    --blue-photo:#0b4fb8;
    --green:#12923f;
    --green-dark:#0c7a31;
    --ink:#1a1a1a;
    --grey-box:#f1f1f1;
    --grey-line:#b5b5b5;
    --white:#ffffff;
  }
  *{margin:0;padding:0;box-sizing:border-box}
  html,body{width:1200px;height:952px;overflow:hidden;background:var(--bg)}
  body{position:relative;font-family:'Roboto',Arial,sans-serif}
  .flyer{position:absolute;top:86px;width:492px;height:748px;background:var(--white);overflow:hidden}
  .flyer--front{left:78px}
  .flyer--back{left:650px}
  .abs{position:absolute}

  /* front */
  .hero-photo{left:0;top:0;width:492px;height:440px;
    background:radial-gradient(ellipse at 60% 30%,#2a7ee0 0%,var(--blue-photo) 45%,#083b8f 100%)}
  .hero-wave{left:0;top:330px;width:492px;height:140px}
  .brand{display:flex;align-items:center;justify-content:center;gap:10px}
  .brand__dot{width:22px;height:22px;border-radius:50%;background:var(--blue)}
  .brand__name{font-family:'Montserrat',sans-serif;font-weight:800;color:var(--blue);letter-spacing:-0.5px}
  .brand__tag{display:flex;align-items:center;gap:6px;font-family:'Roboto',sans-serif;color:#444}
  .brand__tag::before,.brand__tag::after{content:"";height:1px;background:#777;flex:1}
  .front-brand{left:146px;top:465px;width:220px}
  .front-brand .brand__name{font-size:38px}
  .front-brand .brand__tag{font-size:11px;margin-top:2px}
  .headline{left:0;width:492px;text-align:center;font-family:'Montserrat',sans-serif}
  .headline--only{top:568px;font-size:40px;font-weight:500;color:var(--green)}
  .headline--free{top:612px;font-size:78px;font-weight:900;color:var(--blue);letter-spacing:-1px;line-height:1}
  .headline--system{top:683px;font-size:33px;font-weight:500;color:var(--green);letter-spacing:9px;padding-left:9px}
  .foot-stripe{left:0;bottom:0;width:492px;height:14px}

  /* back */
  .top-wave{left:0;top:0;width:492px;height:100px}
  .back-brand{left:318px;top:44px;width:158px}
  .back-brand .brand__name{font-size:26px}
  .back-brand .brand__dot{width:14px;height:14px}
  .back-brand .brand__tag{font-size:8px}
  .thumb{left:37px;width:105px;height:105px;border:3px solid #d6d6d6;border-radius:8px}
  .thumb--equipment{top:140px;background:linear-gradient(135deg,#e9e9ea,#b9bcc0 60%,#8b8f94)}
  .thumb--install{top:266px;background:linear-gradient(135deg,#c9a48a,#dfe4ea 55%,#9aa2ad)}
  .thumb--monitor{top:392px;background:linear-gradient(135deg,#1c2f4d,#3d5f86 55%,#0f1c30)}
  .perk{left:154px;width:301px;border-radius:6px;text-align:center;display:flex;flex-direction:column;justify-content:center}
  .perk--equipment{top:156px;height:78px;background:var(--grey-box);border:1.5px dashed var(--grey-line);
    color:var(--blue);font-weight:700;font-size:19px;line-height:1.18;padding-top:16px}
  .perk--install{top:282px;height:62px;background:var(--green);border:1.5px dashed #5dbb7b;
    color:var(--white);font-weight:700;font-size:24px;padding-top:14px}
  .perk--monitoring{top:410px;height:90px;background:var(--blue);border:1.5px dashed #6f8fcc;color:var(--white);padding-top:14px}
  .perk__lead{font-size:14px;font-weight:400}
  .perk__main{font-family:'Montserrat',sans-serif;font-size:20px;font-weight:900;margin:1px 0}
  .perk__note{font-size:15px}
  .perk-icon{width:50px;height:50px;border-radius:50%;background:#e4e4e4;border:3px solid var(--white);
    box-shadow:0 1px 3px rgba(0,0,0,.3);left:280px;display:flex;align-items:center;justify-content:center}
  .perk-icon--equipment{top:126px}
  .perk-icon--install{top:256px}
  .perk-icon--monitoring{top:384px}
  .how-pill{left:45px;top:524px;width:400px;height:34px;border-radius:10px;background:var(--green-dark);
    border:2px solid #0a5e26;color:var(--white);font-weight:900;font-size:21px;text-align:center;line-height:30px}
  .call-line{left:0;width:492px;text-align:center}
  .call-line--main{top:564px;color:var(--blue);font-weight:900;font-size:20px}
  .call-line--sub{top:590px;color:var(--ink);font-size:20px}
  .phone{left:0;top:612px;width:492px;display:flex;justify-content:center;align-items:center;gap:8px;
    font-family:'Montserrat',sans-serif;font-weight:900;font-size:40px;color:#0d2a12}
  .promo-band{left:0;top:674px;width:492px;height:54px;background:var(--blue);color:var(--white);
    font-family:'Montserrat',sans-serif;font-weight:900;font-size:38px;text-align:center;line-height:54px;letter-spacing:-0.5px}
</style>
</head>
<body>

<section class="flyer flyer--front">
  <div class="abs hero-photo" role="img" aria-label="Hand holding a smartphone with a smart home app, beside a glowing house outline with a padlock"></div>
  <svg class="abs hero-wave" viewBox="0 0 492 140" preserveAspectRatio="none">
    <path d="M0 110 C 0 100, 0 95, 0 110 Z" fill="none"/>
    <path d="M0 70 C 90 130, 200 120, 300 90 C 380 65, 450 60, 492 80 L492 140 L0 140 Z" fill="#ffffff"/>
    <path d="M0 55 C 70 115, 200 115, 300 82 C 380 55, 450 52, 492 70 L492 82 C 450 62, 380 70, 300 96 C 200 126, 80 126, 0 70 Z" fill="#1d4fa3"/>
  </svg>
  <div class="abs front-brand">
    <div class="brand"><span class="brand__dot"></span><span class="brand__name">Shieldwell</span></div>
    <div class="brand__tag">Secure Your Future</div>
  </div>
  <div class="abs headline headline--only">THE ONLY</div>
  <div class="abs headline headline--free">100% FREE</div>
  <div class="abs headline headline--system">SECURITY SYSTEM</div>
  <svg class="abs foot-stripe" viewBox="0 0 492 14" preserveAspectRatio="none">
    <polygon points="0,0 340,0 325,14 0,14" fill="#12923f"/>
    <polygon points="340,0 350,0 335,14 325,14" fill="#ffffff"/>
    <polygon points="350,0 492,0 492,14 335,14" fill="#1d4fa3"/>
  </svg>
</section>

<section class="flyer flyer--back">
  <svg class="abs top-wave" viewBox="0 0 492 100" preserveAspectRatio="none">
    <path d="M0 0 H492 V28 C 420 0, 340 10, 250 50 C 160 90, 60 95, 0 75 Z" fill="#12923f"/>
    <path d="M0 75 C 60 95, 160 90, 250 50 C 340 10, 420 0, 492 28 V36 C 420 10, 340 20, 250 58 C 160 98, 60 100, 0 85 Z" fill="#e6e6e6"/>
  </svg>
  <div class="abs back-brand">
    <div class="brand"><span class="brand__dot"></span><span class="brand__name">Shieldwell</span></div>
    <div class="brand__tag">Secure Your Future</div>
  </div>

  <div class="abs thumb thumb--equipment" role="img" aria-label="Home security equipment: cameras, keypad and sensors"></div>
  <div class="abs perk perk--equipment">$100’S IN FREE PREMIUM<br>SECURITY EQUIPMENT</div>
  <div class="abs perk-icon perk-icon--equipment">
    <svg width="24" height="28" viewBox="0 0 24 28"><path d="M6 12 V8 a6 6 0 0 1 12 0 V12" fill="none" stroke="#333" stroke-width="2"/><rect x="3" y="12" width="18" height="13" rx="2" fill="none" stroke="#333" stroke-width="2"/><circle cx="12" cy="18" r="2" fill="#333"/></svg>
  </div>

  <div class="abs thumb thumb--install" role="img" aria-label="Technician installing a security camera on a brick wall"></div>
  <div class="abs perk perk--install">FREE INSTALLATION</div>
  <div class="abs perk-icon perk-icon--install">
    <svg width="28" height="28" viewBox="0 0 28 28"><path d="M5 5 L23 23 M23 5 L5 23" stroke="#333" stroke-width="3" stroke-linecap="round"/><circle cx="6" cy="6" r="3" fill="none" stroke="#333" stroke-width="2"/></svg>
  </div>

  <div class="abs thumb thumb--monitor" role="img" aria-label="Monitoring centre operator wearing a headset"></div>
  <div class="abs perk perk--monitoring">
    <div class="perk__lead">And what no other company offers...</div>
    <div class="perk__main">ZERO COST MONITORING</div>
    <div class="perk__note">(up to a <b>$74.95</b> per month value)</div>
  </div>
  <div class="abs perk-icon perk-icon--monitoring">
    <svg width="30" height="26" viewBox="0 0 30 26"><rect x="2" y="3" width="20" height="15" rx="1" fill="none" stroke="#333" stroke-width="2"/><polyline points="5,11 9,11 11,7 13,14 15,11 18,11" fill="none" stroke="#333" stroke-width="1.5"/><circle cx="21" cy="17" r="4.5" fill="#e4e4e4" stroke="#333" stroke-width="2"/><line x1="24" y1="20" x2="28" y2="24" stroke="#333" stroke-width="2.5" stroke-linecap="round"/></svg>
  </div>

  <div class="abs how-pill">HOW ARE WE ABLE TO DO THIS?</div>
  <div class="abs call-line call-line--main">CALL OUR 24-HOUR MESSAGE LINE</div>
  <div class="abs call-line call-line--sub">FOR A 2-MINUTE OVERVIEW</div>
  <div class="abs phone">
    <svg width="30" height="30" viewBox="0 0 30 30"><circle cx="15" cy="15" r="13" fill="none" stroke="#12923f" stroke-width="2"/><path d="M12 8 C 9 10, 9 20, 12 22 L14 20 L13 17 L12 15 L13 12 L14 10 Z" fill="#12923f"/></svg>
    <span class="phone__number">0100 246 810</span>
  </div>
  <div class="abs promo-band">100% FREE SECURITY</div>
  <svg class="abs foot-stripe" viewBox="0 0 492 14" preserveAspectRatio="none">
    <polygon points="0,0 340,0 325,14 0,14" fill="#12923f"/>
    <polygon points="340,0 350,0 335,14 325,14" fill="#ffffff"/>
    <polygon points="350,0 492,0 492,14 335,14" fill="#1d4fa3"/>
  </svg>
</section>

</body>
</html>
```